Poster for a series of live music events

Looking for a simplistic poster design for live music gigs. I would like something that i can reuse by moving the positioning of the words on the poster and the colour scheme. Attached is an example of a design that i like. The size should be A4.
File format preferred would be photoshop.
Text in the poster is not that important at this stage as it is just a template i am after. But it should include band names, location, date and time. So feel free to make up the text. The file provided in the brief will show you the similar things that will be included.

```html
<!DOCTYPE html>
<html lang="en">
<head>
<meta charset="utf-8">
<title>Let's Party – Band Group</title>
<link rel="stylesheet" href="https://fonts.googleapis.com/css2?family=Righteous&family=Questrial&family=Libre+Baskerville&display=swap">
<style>
  :root {
    --ink-purple: #3b3482;
    --deep-purple: #2a2266;
    --glow-cyan: #1fb8dc;
    --paper: #ffffff;
    --night: #0b0a14;
    --violet: #7a2fb8;
    --magenta: #c0359a;
    --amber: #f2b22a;
    --lime: #b9e23a;
    --aqua: #22c7d8;
  }
  html, body {
    margin: 0;
    padding: 0;
    width: 848px;
    height: 1200px;
    overflow: hidden;
    background: var(--paper);
  }
  .poster {
    position: relative;
    width: 848px;
    height: 1200px;
    overflow: hidden;
  }
  .stage-art {
    position: absolute;
    inset: 0 0 180px 0;
    background:
      radial-gradient(ellipse 420px 300px at 20% 8%, var(--violet) 0%, transparent 70%),
      radial-gradient(ellipse 380px 260px at 55% 6%, var(--magenta) 0%, transparent 72%),
      radial-gradient(ellipse 360px 340px at 90% 28%, var(--amber) 0%, transparent 70%),
      radial-gradient(ellipse 300px 240px at 12% 62%, var(--aqua) 0%, transparent 72%),
      radial-gradient(ellipse 340px 260px at 70% 60%, var(--lime) 0%, transparent 70%),
      linear-gradient(180deg, #5a2a9a 0%, #8a3a8a 30%, #3a7aa0 55%, #1a1a2a 72%, var(--night) 90%);
  }
  .layout {
    position: absolute;
    inset: 0;
  }
  .headline {
    font-family: "Righteous", sans-serif;
    fill: var(--paper);
    paint-order: stroke fill;
    stroke-linejoin: round;
  }
  .headline--cyan { stroke: var(--glow-cyan); }
  .headline--band { stroke: var(--deep-purple); }
  .band-strip { fill: var(--ink-purple); }
  .info-panel { fill: var(--paper); }
  .tagline {
    font-family: "Questrial", sans-serif;
    fill: var(--paper);
  }
  .ticket {
    font-family: "Questrial", sans-serif;
    fill: var(--ink-purple);
  }
  .details {
    font-family: "Libre Baskerville", serif;
    fill: var(--ink-purple);
    text-anchor: middle;
  }
  .divider {
    stroke: var(--ink-purple);
    stroke-width: 3;
  }
</style>
</head>
<body>
<main class="poster">
  <div class="stage-art" role="img" aria-label="Colourful club lights with equalizer bars, a pair of headphones and a cheering crowd in silhouette"></div>

  <svg class="layout" viewBox="0 0 848 1200" width="848" height="1200">
    <text class="headline headline--cyan" x="48" y="210" font-size="64" stroke-width="12" textLength="205" lengthAdjust="spacingAndGlyphs">LET'S</text>
    <text class="headline headline--cyan" x="46" y="384" font-size="205" stroke-width="16" textLength="770" lengthAdjust="spacingAndGlyphs">PARTY</text>
    <text class="headline headline--band" x="48" y="478" font-size="92" stroke-width="14" textLength="750" lengthAdjust="spacingAndGlyphs">BAND GROUP</text>

    <polygon class="info-panel" points="0,996 848,858 848,1200 0,1200"/>
    <polygon class="band-strip" points="90,924 848,792 848,858 0,996 0,950"/>
    <polygon class="band-strip" points="0,1200 848,1150 848,1200"/>

    <text class="tagline" x="100" y="968" font-size="54" transform="rotate(-8 100 968)" textLength="720" lengthAdjust="spacingAndGlyphs">LIVE&#160;&#160;ENTERTAINMENT</text>
    <text class="ticket" x="630" y="918" font-size="27" transform="rotate(-8 630 918)">TICKET PRICE</text>

    <line class="divider" x1="237" y1="1026" x2="237" y2="1164"/>
    <line class="divider" x1="600" y1="1026" x2="600" y2="1164"/>

    <text class="details" x="114" y="1074" font-size="44">JULY</text>
    <text class="details" x="114" y="1118" font-size="44">23</text>
    <text class="details" x="114" y="1162" font-size="44">2015</text>

    <text class="details" x="420" y="1128" font-size="78">VENUE</text>

    <text class="details" x="722" y="1046" font-size="24">DOORS OPEN</text>
    <text class="details" x="722" y="1094" font-size="44">9 PM</text>
    <text class="details" x="722" y="1138" font-size="44">2AM</text>
  </svg>
</main>
</body>
</html>
```